Website Redesign
Maritime Logistics and Shipping Company
Website Redesign - Transportation
Creative Brief
Transportation
www.volterafreight.example
Voltera Freight specializes in the transport of mineral resources from emerging markets to other parts of the world. It also provides seaborne shipping solutions and bulk cargo logistics. We are looking to enhance our website. Presenting a world-class/professional look is of the utmost importance to us.
We are looking for simple formats (maybe one high quality picture of a ship in the background with tabs that display varying text when clicked). Here are some other sites to get ideas from as well: www.harbor.pelmarock.example; www.gq-vastmar.example; www.qfzorvanite.example. Please use high quality pictures of bulk carrier ships and professional fonts.
High Tech
Arial, Times New Roman, Century Gothic
below header
www.harbor.pelmarock.example
www.qfzorvanite.example
www.gq-vastmar.example
We also would be open to formats used in this posting: http://www.quillaspark.example/contests/brenwick-drillsite-gear-depot-web-template

```html
<!DOCTYPE html>
<html lang="fr">
<head>
<meta charset="utf-8">
<title>Voltera Freight – Compagnie Guinéenne de Transport Maritime</title>
<link href="https://fonts.googleapis.com/css2?family=Arimo:wght@400;700&display=swap" rel="stylesheet">
<style>
:root{
  --page:#f3f3f3;
  --brand-red:#c8161d;
  --brand-green:#2f7d32;
  --brand-gold:#f2c21a;
  --nav-blue:#5a8fc4;
  --nav-blue-dark:#3f72a8;
  --hero-light:#b7d2ec;
  --hero-mid:#6f9fd0;
  --hero-deep:#2f5c99;
  --text:#555555;
  --card-bg:#ffffff;
  --card-border:#dcdcdc;
  --footer:#3a3a3a;
  --footer-text:#dddddd;
  --white:#ffffff;
}
*{box-sizing:border-box;margin:0;padding:0}
html,body{width:1200px;height:901px;overflow:hidden}
body{position:relative;background:linear-gradient(#ececec,#fafafa 30%,#f1f1f1);font-family:"Arimo",Arial,sans-serif;color:var(--text)}
.top-rule{position:absolute;left:0;top:0;width:1200px;height:5px;background:var(--brand-red)}
.brand{position:absolute;left:110px;top:30px;display:flex;align-items:center;gap:14px}
.brand-mark{width:80px;height:80px;border-radius:50%;background:var(--brand-gold)}
.brand-name{font-weight:700;font-size:36px;color:var(--brand-green);letter-spacing:1px;line-height:1}
.phone{position:absolute;left:803px;top:19px;width:231px;height:42px;border-radius:8px;background:linear-gradient(#fdfdfd,#dcdcdc);border:1px solid #c9c9c9;display:flex;align-items:center;justify-content:center;gap:12px;font-size:23px;color:#333}
.lang{position:absolute;left:1059px;top:22px;width:36px;height:36px;border-radius:50%;background:#2b3f86;border:2px solid #fff;box-shadow:0 0 2px #999}
.nav{position:absolute;left:107px;top:134px;width:988px;height:36px;border-bottom:3px solid var(--nav-blue);display:flex;gap:5px}
.nav a{display:block;height:36px;padding:0 17px;line-height:36px;font-size:15px;font-weight:700;color:#333;text-decoration:none;background:linear-gradient(#fff,#ececec);border:1px solid #d2d2d2;border-bottom:none;border-radius:4px 4px 0 0;text-transform:uppercase}
.nav a.active{background:linear-gradient(var(--nav-blue),var(--nav-blue-dark));color:var(--white);border-color:var(--nav-blue-dark)}
.hero{position:absolute;left:107px;top:173px;width:988px;height:404px;overflow:hidden;box-shadow:0 14px 16px -10px rgba(0,0,0,.35)}
.hero-photo{position:absolute;inset:0;background:linear-gradient(160deg,var(--hero-light) 0%,var(--hero-mid) 55%,var(--hero-deep) 100%)}
.hero-title{position:absolute;left:36px;top:56px;font-size:29px;font-weight:400;line-height:37px;color:var(--white)}
.hero-title span{display:block;color:var(--brand-red)}
.hero-arrow{position:absolute;top:184px;width:34px;height:34px;background:#333;border-radius:3px;display:flex;align-items:center;justify-content:center}
.hero-arrow.prev{left:0}.hero-arrow.next{right:0}
.cards{position:absolute;left:107px;top:613px;width:988px;display:flex;justify-content:space-between}
.card{width:318px;height:215px;background:var(--card-bg);border:1px solid var(--card-border);border-radius:6px;padding:8px 12px;box-shadow:0 2px 4px rgba(0,0,0,.1)}
.card-head{display:inline-flex;align-items:center;gap:10px;height:37px;padding:0 16px 0 6px;border-radius:6px;background:linear-gradient(#fafafa,#dedede);border:1px solid #cfcfcf;font-size:18px;color:var(--brand-red)}
.card-icon{width:28px;height:28px;border-radius:50%;background:var(--brand-gold)}
.card p{margin-top:6px;font-size:13px;line-height:19.5px}
.card p b{font-weight:400;color:var(--brand-red)}
.read-more{display:inline-block;margin-top:6px;padding:3px 10px;font-size:12px;color:#444;background:linear-gradient(#fff,#dcdcdc);border:1px solid #c5c5c5;border-radius:4px}
.footer{position:absolute;left:0;top:852px;width:1200px;height:49px;background:var(--footer);border-top:3px solid var(--brand-red);color:var(--footer-text);font-size:13px}
.footer .copy{position:absolute;left:110px;top:14px}
.footer .links{position:absolute;left:880px;top:14px;word-spacing:2px}
</style>
</head>
<body>
<div class="top-rule"></div>
<header>
  <div class="brand"><span class="brand-mark"></span><span class="brand-name">VOLTERA FREIGHT</span></div>
  <div class="phone">
    <svg width="26" height="22" viewBox="0 0 26 22"><path d="M2 6c0-3 4-5 11-5s11 2 11 5l-5 2-1-3c-3-1-7-1-10 0l-1 3zM6 10h14l3 10H3z" fill="#333"/></svg>
    (224).55.01.27.88
  </div>
  <div class="lang" role="img" aria-label="Choix de langue : anglais"></div>
</header>
<nav class="nav">
  <a class="active" href="#">Accueil</a>
  <a href="#">La Compagnie</a>
  <a href="#">Resources Humaines</a>
  <a href="#">Oeuvres Social</a>
  <a href="#">Clients</a>
  <a href="#">Contact</a>
</nav>
<section class="hero">
  <div class="hero-photo" role="img" aria-label="Photo d'un vraquier en mer sous un ciel bleu"></div>
  <h1 class="hero-title">Compagnie Guinéene<span>de Transport Maritime</span></h1>
  <div class="hero-arrow prev"><svg width="14" height="14" viewBox="0 0 14 14"><path d="M10 2 3 7l7 5z" fill="#fff"/></svg></div>
  <div class="hero-arrow next"><svg width="14" height="14" viewBox="0 0 14 14"><path d="M4 2l7 5-7 5z" fill="#fff"/></svg></div>
</section>
<section class="cards">
  <article class="card">
    <div class="card-head"><span class="card-icon"></span>Mission</div>
    <p><b>Voltera Freight (TVR)</b> se spécialise dans le transport du minerai Guinéen, jusqu'aux installations de traitement en Amérique, en Europe, en Australie, et d'autres parties du monde. L'objectif principal de la société est d'offrir des services efficients...</p>
    <span class="read-more">Read More</span>
  </article>
  <article class="card">
    <div class="card-head"><span class="card-icon"></span>La Compagnie</div>
    <p><b>Voltera Freight</b> est le produit de Guinéens qui ont pendant plusieurs décennies été intimement associés à la supervision de toute la logistique du transport maritime d'une vaste gamme de produits et une grande variété de...</p>
    <span class="read-more">Read More</span>
  </article>
  <article class="card">
    <div class="card-head"><span class="card-icon"></span>Philosophie</div>
    <p>Détenue et gérée par des ressortissants guinéens, <b>Voltera Freight</b> est solidement déterminée à participer à la croissance du commerce international Guinéen. La société ambitionne d'utiliser sa vaste expérience maritime et son immense réseau...</p>
    <span class="read-more">Read More</span>
  </article>
</section>
<footer class="footer">
  <span class="copy">Copyright © 2011 volterafreight.example All Rights Reserved.</span>
  <span class="links">Privacy Policy &nbsp;|&nbsp; Terms &amp; Conditions</span>
</footer>
</body>
</html>
```